Erstellung einer ersten Einladungskarte „Safe the Date“
Zielgruppe
Spezialist für temporäres Linienmanagement & Projektmanagement
Als Sozietät für professionelles Interim Management bündelt die brückwerk AG die fachliche Kompetenz und die langjährige Erfahrung erfolgreicher Führungspersönlichkeiten aus nahezu allen Sektoren der Wirtschaft. Wir unterstützen unsere Kunden bei der Bewältigung temporärer Herausforderungen im Linienmanagement sowie im Management komplexer strategischer Projekte und Programme.
https://www.brueckwerk-example.net/de/home.html
Aufgabenstellung
Siehe angehängtes Briefing und angehängtes CD Manual, das nicht zwingend eingehalten werden muss für diesen Job

```html
<!DOCTYPE html>
<html lang="de">
<head>
<meta charset="utf-8">
<title>Safe the Date – brückwerk AG</title>
<link rel="stylesheet" href="https://fonts.googleapis.com/css2?family=Michroma&family=Roboto:wght@400&display=swap">
<style>
  :root {
    --board: #dcdcde;
    --orange: #e86513;
    --teal: #3d6a80;
    --white: #ffffff;
    --label: #8a8a8c;
    --black: #000000;
    --fruit-light: #fbc24a;
    --fruit-mid: #f39a1f;
    --fruit-pale: #f7b46a;
  }
  * { box-sizing: border-box; margin: 0; padding: 0; }
  html, body { width: 938px; height: 1200px; overflow: hidden; }
  body {
    background: var(--board);
    font-family: "Michroma", "Arial", sans-serif;
    position: relative;
  }
  .card {
    position: absolute;
    left: 75px;
    width: 788px;
    height: 376px;
    box-shadow: 6px 8px 12px rgba(0,0,0,0.22);
  }
  .card--front { top: 75px; background: var(--orange); }
  .card--back { top: 541px; background: var(--white); }

  .wordmark {
    position: absolute;
    right: 52px;
    font-size: 28px;
    letter-spacing: -0.5px;
    color: var(--teal);
    line-height: 1;
    white-space: nowrap;
  }
  .card--front .wordmark { top: 41px; }
  .card--back .wordmark { top: 302px; }

  .art-half-orange {
    position: absolute;
    left: 266px; top: 43px;
    width: 220px; height: 195px;
    border-radius: 10px;
    background: linear-gradient(160deg, var(--fruit-pale) 0%, var(--fruit-light) 45%, var(--fruit-mid) 100%);
  }
  .headline {
    position: absolute;
    left: 54px; top: 254px;
    font-size: 74px;
    font-weight: 400;
    color: var(--white);
    letter-spacing: 1px;
    white-space: nowrap;
    line-height: 1;
  }
  .front-date {
    position: absolute;
    right: 59px; top: 333px;
    font-size: 13px;
    color: var(--white);
    font-style: italic;
    letter-spacing: 1px;
    white-space: nowrap;
  }

  .board-label {
    position: absolute;
    font-family: "Roboto", "Arial", sans-serif;
    font-size: 18.5px;
    line-height: 1;
    color: var(--label);
  }
  .board-label--front { right: 128px; top: 478px; }
  .board-label--back { right: 130px; top: 946px; }
  .board-label--icon { left: 639px; top: 1069px; }

  .motto {
    position: absolute;
    left: 50px; top: 46px;
    font-size: 45.5px;
    font-weight: 400;
    color: var(--orange);
    white-space: nowrap;
    line-height: 1;
  }
  .art-orange {
    position: absolute;
    left: 46px; top: 118px;
    width: 215px; height: 222px;
    border-radius: 10px;
    background: linear-gradient(160deg, #7fae6f 0%, var(--fruit-light) 35%, var(--fruit-mid) 100%);
  }
  .invite { color: var(--teal); font-style: italic; }
  .invite__lead {
    position: absolute;
    left: 294px; top: 135px;
    font-size: 18.3px; line-height: 22px; letter-spacing: 0.5px;
    text-indent: 5px;
    white-space: nowrap;
  }
  .invite__facts {
    position: absolute;
    left: 289px; top: 193px;
    font-size: 15.9px; line-height: 21px;
    white-space: nowrap;
  }
  .invite__facts dt { display: inline-block; width: 70px; }
  .invite__facts dd { display: inline; color: var(--orange); }
  .invite__facts dd::after { content: "\A"; white-space: pre; }
  .invite__note {
    position: absolute;
    left: 275px; top: 244px;
    font-size: 12.6px; line-height: 18px; letter-spacing: 0.3px;
    white-space: nowrap;
  }

  .icon-tile {
    position: absolute; top: 1027px;
    width: 100px; height: 101px;
  }
  .icon-tile--plain { left: 313px; background: transparent; }
  .icon-tile--light { left: 411px; background: var(--white); }
  .icon-tile--dark { left: 517px; background: var(--black); }
  .icon-tile .art {
    position: absolute; left: 10px; top: 8px;
    width: 82px; height: 85px;
    border-radius: 8px;
    background: linear-gradient(160deg, #7fae6f 0%, var(--fruit-light) 35%, var(--fruit-mid) 100%);
  }
</style>
</head>
<body>
  <section class="card card--front">
    <div class="art-half-orange" role="img" aria-label="Aquarell einer halbierten Orange"></div>
    <div class="wordmark">brückwerk</div>
    <h1 class="headline">Safe the Date</h1>
    <p class="front-date">1. und 2. Dezember 2017</p>
  </section>
  <p class="board-label board-label--front">Vorderseite</p>

  <section class="card card--back">
    <h2 class="motto">«Ein Hauch von Orange»</h2>
    <div class="art-orange" role="img" aria-label="Aquarell einer ganzen Orange mit Blatt"></div>
    <div class="invite">
      <p class="invite__lead">Die brückwerk AG wird 10 Jahre alt,<br>das werden wir feiern.</p>
      <dl class="invite__facts">
        <dt>Wann:</dt><dd>1. und 2. Dezember 2017</dd>
        <dt>Wo:</dt><dd>München</dd>
      </dl>
      <p class="invite__note">Details zur Feier sowie Möglichkeiten zur Übernachtung<br>in München werden wir rechtzeitig vor der Feier mitteilen.</p>
    </div>
    <div class="wordmark">brückwerk</div>
  </section>
  <p class="board-label board-label--back">Rückseite</p>

  <div class="icon-tile icon-tile--plain"><div class="art" role="img" aria-label="Icon: Orange mit Blatt, freigestellt"></div></div>
  <div class="icon-tile icon-tile--light"><div class="art" role="img" aria-label="Icon: Orange mit Blatt auf Weiß"></div></div>
  <div class="icon-tile icon-tile--dark"><div class="art" role="img" aria-label="Icon: Orange mit Blatt auf Schwarz"></div></div>
  <p class="board-label board-label--icon">Icon</p>
</body>
</html>
```